CD cover - Horizons: Ample Room To Share

Welcome!

The album contains acoustic music with positive and affirmative lyrics.

Here's a medley of some songs.
https://files.wavecrate-example.net/u/83610457/bela_morvik_ample_room_to_share_20150220.mp3

This music and life style is about enjoying ourselves and this game we call life. Respect, gratitude, love, forgiveness, simplicity, together these lead to a happy, blissful life. If the potential listener - when looking at the cover - gets this message, than it's perfect. Just make it simple, playful, beautiful. :)

BUT PLEASE AVOID CLICHÉS!! Come up with something original! Thank you!

Note: the front cover in case of online purchase of the album will be shown on a cell-phone for example. If the image is complicated and too detailed, it won't look like something.

The CD cover project has 4 parts:
1. CD cover front outside
2. CD cover front inside (track list)
3. CD cover back
4. CD (print on the disc)

The performer: Bela Morvik (logo attached). Please use the logo with the original colors and design the cover to go well with it.

Album title: Horizons: Ample Room To Share
All my upcoming albums are going to be called "Horizons: something"

Track list:
1. Warm (3:49)
2. Hope For Many (3:48)
3. We Will Rise (4:36)
4. Sunny Road (2:54)
5. Letting Go (2:58)
6. Weightless (3:41)
7. Wonderful (3:23)
8. Thankful Heart (4:03)
9. Calm & Kindness (3:39)
10. Quiet Harbor (4:03)
11. Softly Now (4:38)
12. Open Skies (4:17)

All songs written by Bela Morvik
Copyright Belasound 2015.
www.belasound-example.net

I am going to need the cover in RGB format.

That's pretty much it. If I missed something important, mail me without hesitation! Enjoy! :)

Target Market(s)

New Age spiritual people, positive thinking people.

Industry/Entity Type

Cell Phone

Requirements
Must have
• Easy to read text and logo. I'm still building the brand.
Nice to have
• Light colors
Should not have
• Any kind of negativity at all.

```html
<!DOCTYPE html>
<html lang="en">
<head>
<meta charset="utf-8">
<title>Horizons: Ample Room To Share – CD Cover</title>
<link rel="stylesheet" href="https://fonts.googleapis.com/css2?family=Montserrat:wght@300;400;600&display=swap">
<style>
  :root {
    --page-bg: #e9eaee;
    --sky-deep: #2a6cc4;
    --sky-mid: #6fa7e0;
    --sky-pale: #d6e8f6;
    --sun-glow: #fbfbf4;
    --haze: #efe6cc;
    --wheat-light: #d7a447;
    --wheat-mid: #a86f22;
    --wheat-deep: #6e4314;
    --wheat-dark: #3a220a;
    --title-white: #ffffff;
    --mark-ink: #1c1309;
    --mark-disc: rgba(255, 244, 214, 0.55);
  }
  * { margin: 0; padding: 0; box-sizing: border-box; }
  html, body {
    width: 1200px;
    height: 800px;
    overflow: hidden;
    background: var(--page-bg);
  }
  .canvas {
    position: relative;
    width: 1200px;
    height: 800px;
  }
  .cover {
    position: absolute;
    left: 240px;
    top: 40px;
    width: 720px;
    height: 720px;
    overflow: hidden;
    font-family: "Montserrat", sans-serif;
  }
  .cover-photo {
    position: absolute;
    inset: 0;
    background:
      radial-gradient(ellipse 70% 30% at 45% 58%, var(--sun-glow) 0%, rgba(251, 251, 244, 0) 100%),
      radial-gradient(ellipse 90% 40% at 50% 100%, rgba(58, 34, 10, 0.55) 0%, rgba(58, 34, 10, 0) 100%),
      linear-gradient(180deg,
        var(--sky-deep) 0%,
        var(--sky-mid) 24%,
        var(--sky-pale) 46%,
        var(--sun-glow) 56%,
        var(--haze) 63%,
        var(--wheat-light) 71%,
        var(--wheat-mid) 82%,
        var(--wheat-deep) 92%,
        var(--wheat-dark) 100%);
  }
  .album-title {
    position: absolute;
    top: 74px;
    left: 0;
    width: 100%;
    text-align: center;
    color: var(--title-white);
    text-shadow: 0 1px 6px rgba(20, 60, 120, 0.25);
  }
  .album-title .series {
    display: block;
    font-weight: 600;
    font-size: 42px;
    letter-spacing: 0.22em;
    line-height: 1;
    padding-left: 0.22em;
  }
  .album-title .subtitle {
    display: block;
    margin-top: 8px;
    font-weight: 300;
    font-size: 42px;
    letter-spacing: 0.01em;
    line-height: 1.1;
  }
  .artist-mark {
    position: absolute;
    left: 50%;
    top: 588px;
    transform: translateX(-50%);
    display: flex;
    flex-direction: column;
    align-items: center;
    gap: 10px;
    color: var(--mark-ink);
    font-weight: 400;
    font-size: 30px;
    line-height: 1;
    white-space: nowrap;
  }
  .artist-mark .disc {
    width: 44px;
    height: 44px;
    border-radius: 50%;
    background: var(--mark-disc);
  }
</style>
</head>
<body>
  <main class="canvas">
    <section class="cover">
      <div class="cover-photo" role="img" aria-label="Photograph of golden wheat ears swaying in a field under a bright blue sky"></div>
      <h1 class="album-title">
        <span class="series">HORIZONS</span>
        <span class="subtitle">Ample Room To Share</span>
      </h1>
      <div class="artist-mark">
        <span class="disc"></span>
        <span class="artist-name">Bela Morvik</span>
      </div>
    </section>
  </main>
</body>
</html>
```